Maple Lantern Business Card

Design of business cards

Target Market(s)

We are aiming as small business owners who need anything from basic business structures, website plans, business processes and quality assurance.

Industry/Entity Type

Business

Colors

Designer to choose colors to be used in the design.

Requirements
Nice to have
• I would prefer one side of the card to use the green from the logo. Prefer to have the same font as the logo.

```html
<!DOCTYPE html>
<html lang="en">
<head>
<meta charset="utf-8">
<title>Maple Lantern Consulting – Business Card</title>
<link rel="stylesheet" href="https://fonts.googleapis.com/css2?family=Marcellus&family=Open+Sans:wght@400;600&display=swap">
<style>
  :root {
    --page: #2b2b2b;
    --card-white: #f1f1ef;
    --brand-green: #84b51f;
    --brand-green-deep: #76a316;
    --ink-grey: #3c3c3c;
    --on-green: #eef6dc;
    --shadow: rgba(0, 0, 0, 0.45);
  }
  * { box-sizing: border-box; margin: 0; padding: 0; }
  html, body {
    width: 1200px;
    height: 900px;
    overflow: hidden;
    background: var(--page);
  }
  .canvas {
    width: 1200px;
    height: 900px;
    display: flex;
    flex-direction: column;
    align-items: center;
    justify-content: center;
    gap: 60px;
  }
  .card {
    width: 630px;
    height: 360px;
    position: relative;
    box-shadow: 0 12px 30px var(--shadow);
  }

  /* Front: wordmark on white */
  .card--front {
    background: var(--card-white);
    display: flex;
    align-items: center;
    justify-content: center;
  }
  .wordmark {
    display: flex;
    align-items: center;
    gap: 26px;
  }
  .wordmark__dot {
    width: 74px;
    height: 74px;
    border-radius: 50%;
    background: var(--brand-green);
    flex: none;
  }
  .wordmark__name {
    font-family: "Marcellus", serif;
    color: var(--brand-green);
    font-size: 34px;
    line-height: 1.08;
    letter-spacing: 0.02em;
    text-transform: uppercase;
    font-variant: small-caps;
  }

  /* Back: contact details on green */
  .card--back {
    background: var(--brand-green);
    font-family: "Open Sans", sans-serif;
    color: var(--on-green);
  }
  .contact {
    position: absolute;
    left: 48px;
    bottom: 44px;
    font-size: 14px;
    line-height: 1.35;
  }
  .contact__name {
    font-weight: 600;
    font-size: 17px;
  }
  .contact__role {
    margin-bottom: 16px;
  }
  .contact__label { font-weight: 600; }
  .contact__web { margin-top: 14px; }
  .card__blind-name {
    position: absolute;
    right: 52px;
    bottom: 92px;
    font-family: "Marcellus", serif;
    font-size: 26px;
    color: var(--brand-green-deep);
    text-transform: uppercase;
  }
</style>
</head>
<body>
  <main class="canvas">
    <section class="card card--front" aria-label="Card front">
      <div class="wordmark">
        <span class="wordmark__dot" aria-hidden="true"></span>
        <p class="wordmark__name">Maple<br>Lantern<br>Consulting</p>
      </div>
    </section>

    <section class="card card--back" aria-label="Card back">
      <div class="contact">
        <p class="contact__name">Jordan Avery</p>
        <p class="contact__role">Managing Director, Operations</p>
        <p>48 Birchwood Lane, Eastmere</p>
        <p><span class="contact__label">E:</span> javery@maplelantern.com</p>
        <p><span class="contact__label">P:</span> 555-014-2290 <span class="contact__label">M:</span> 555-014-7731</p>
        <p class="contact__web">www.maplelantern.com</p>
      </div>
      <p class="card__blind-name">Maple Lantern</p>
    </section>
  </main>
</body>
</html>
```